Copper Gulls Broken Lantern Hour vol. 2

The band Copper Gulls in Texas needs an album cover featuring:

There are 4 heads of the white power system:
- a CEO / politician
- a ZQL member
- a cop
- a judge.

Their faces are power outlets.

A multicultural fist unplugging the power cords from the outlets.

It is OPTIONAL to include the title on the CD cover:
"Copper Gulls, Broken Lantern Hour, vol. 2"
If it fits and looks cool, include the lettering. If it doesn't fit, that's fine too.

Check out the cover of Broken Lantern Hour, vol. 1 by Marta Velloni. That album (volume 1) is already released, you are designing a cover for volume 2.

Target Market(s)

Quiet Orchard Union, Hip Hop, Funk

Industry/Entity Type

Music Download

Logo Text

no logo

Font styles to use
Serif

Requirements
Must have
• 4 heads of the white power system (a CEO / politician. a ZQL member, a cop, a judge), NO faces, just power outlets

A multicultural fist, or fists, unplugging the power cords from the outlets.

400 dpi minimum 600 dpi preferred 5"x 5" printable area with 0.25" bleed
Nice to have
• hip hop graffiti style is probably a good way to go, but we're open to other directions too
Should not have
• Do NOT include any text other than:
Copper Gulls
Broken Lantern Hour, vol. 2
Do not include faces, their faces are replaced with power outlets

```html
<!DOCTYPE html>
<html lang="en">
<head>
<meta charset="utf-8">
<title>Copper Gulls – Broken Lantern Hour Vol. 2</title>
<link rel="stylesheet" href="https://fonts.googleapis.com/css2?family=Permanent+Marker&family=Sedgwick+Ave+Display&display=swap">
<style>
  :root {
    --page: #ffffff;
    --night: #0d0e16;
    --ray-dark: #1d1c1e;
    --ray-light: #3a3a3d;
    --haze: #8d8d90;
    --lime: #c6e04a;
    --ink: #17181f;
    --chalk: #ffffff;
    --sky: #27b5e8;
    --flame: #f0531c;
    --scarlet: #e2232a;
    --sun: #c3d545;
    --art-violet: #9189c8;
    --art-rose: #b0707a;
    --art-teal: #6fa8a3;
    --art-brown: #8a6440;
    --art-pink: #e6a9d0;
  }
  * { margin: 0; padding: 0; box-sizing: border-box; }
  html, body { width: 879px; height: 1200px; overflow: hidden; background: var(--page); }

  .album-cover {
    position: absolute;
    left: 50px; top: 210px;
    width: 780px; height: 780px;
    overflow: hidden;
    background: repeating-conic-gradient(from 0deg at 50% 40%, var(--ray-dark) 0deg 8deg, var(--ray-light) 8deg 12deg);
  }
  .album-cover::before {
    content: ""; position: absolute; inset: 0;
    background:
      linear-gradient(100deg, transparent 50%, rgba(141,141,144,.5) 100%),
      radial-gradient(circle at 50% 40%, rgba(0,0,0,.6) 0 28%, transparent 62%);
  }

  .layer { position: absolute; left: 0; top: 0; width: 780px; height: 780px; }

  .cover-art {
    position: absolute; left: 205px; top: 92px; width: 385px; height: 410px;
    border-radius: 42% 46% 38% 44%;
    background:
      radial-gradient(circle at 52% 46%, var(--art-pink) 0 9%, transparent 17%),
      radial-gradient(ellipse at 28% 30%, var(--art-teal) 0 26%, transparent 48%),
      radial-gradient(ellipse at 76% 30%, var(--art-violet) 0 28%, transparent 50%),
      radial-gradient(ellipse at 70% 72%, var(--art-rose) 0 24%, transparent 46%),
      radial-gradient(ellipse at 30% 74%, var(--art-brown) 0 22%, transparent 44%),
      #5b5670;
  }

  .crowd-haze {
    position: absolute; left: 0; right: 0; top: 540px; height: 90px;
    background: linear-gradient(to bottom, transparent, rgba(141,141,144,.55) 55%, transparent);
  }
  .crowd {
    position: absolute; left: 0; right: 0; bottom: 0; height: 270px;
    background: linear-gradient(to bottom, rgba(13,14,22,0) 0, rgba(13,14,22,.8) 14%, var(--night) 34%);
  }

  .album-title {
    position: absolute; left: 0; right: 0; top: 548px;
    text-align: center;
    font-family: "Sedgwick Ave Display", "Permanent Marker", cursive;
    font-size: 80px; line-height: 1; letter-spacing: 3px;
    font-weight: 400;
    color: var(--lime);
    transform: rotate(-2deg);
  }
  .album-subtitle {
    position: absolute; left: 0; right: 0; top: 650px;
    text-align: center;
    font-family: "Permanent Marker", cursive;
    font-size: 38px; line-height: 1; letter-spacing: 2px;
    text-transform: uppercase;
    color: var(--chalk);
    -webkit-text-stroke: 1.5px var(--ink);
  }
  .volume-badge {
    position: absolute; left: 309px; top: 707px; width: 156px; height: 47px;
    border-radius: 8px; background: var(--lime);
    display: flex; align-items: center; justify-content: center;
    font-family: "Permanent Marker", cursive; font-size: 28px; color: var(--ink);
  }
</style>
</head>
<body>
  <main class="album-cover">
    <svg class="layer burst" viewBox="0 0 780 780" aria-hidden="true">
      <defs>
        <radialGradient id="burst-core" cx="50%" cy="50%" r="50%">
          <stop offset="0" stop-color="#3a3a30"/>
          <stop offset="1" stop-color="#1b1b1c"/>
        </radialGradient>
      </defs>
      <polygon fill="url(#burst-core)" stroke="var(--lime)" stroke-width="11" stroke-linejoin="round"
        points="630,300 590,345 607,402 551,425 541,484 482,480 447,529 395,500 343,529 308,480 249,484 239,425 183,402 200,345 160,300 200,255 183,198 239,175 249,116 308,120 343,71 395,100 447,71 482,120 541,116 551,175 607,198 590,255"/>
    </svg>

    <div class="cover-art" role="img" aria-label="Illustration: four figures with power-outlet heads – a politician, a hooded member, a cop and a judge – around a multicoloured fist unplugging their cords"></div>

    <svg class="layer sparks" viewBox="0 0 780 780" aria-hidden="true">
      <defs>
        <polygon id="star" points="0,-14 4,-4.5 14,-4.3 6,2 9,12 0,6 -9,12 -6,2 -14,-4.3 -4,-4.5"/>
        <polygon id="bolt" points="-30,-6 -8,-14 -10,-4 12,-12 10,-2 32,-10 8,8 10,-2 -12,6 -10,-4"/>
      </defs>
      <use href="#star" fill="var(--sun)" transform="translate(364,49)"/>
      <use href="#star" fill="var(--scarlet)" transform="translate(457,59)"/>
      <use href="#star" fill="var(--chalk)" transform="translate(172,159) scale(1.4)"/>
      <use href="#star" fill="var(--scarlet)" transform="translate(145,399)"/>
      <use href="#star" fill="var(--scarlet)" transform="translate(629,399) scale(1.6)"/>
      <use href="#star" fill="var(--scarlet)" transform="translate(552,502) scale(1.2)"/>
      <use href="#star" fill="var(--chalk)" transform="translate(261,541) scale(.6)"/>
      <use href="#star" fill="var(--chalk)" transform="translate(489,551) scale(.6)"/>

      <use href="#bolt" fill="var(--sky)" transform="translate(207,74) rotate(20) scale(1.1)"/>
      <use href="#bolt" fill="var(--flame)" transform="translate(542,84) rotate(-60) scale(1.4)"/>
      <use href="#bolt" fill="var(--sky)" transform="translate(627,139) rotate(-55) scale(1.1)"/>
      <use href="#bolt" fill="var(--flame)" transform="translate(122,279) rotate(15) scale(1.5)"/>
      <use href="#bolt" fill="var(--flame)" transform="translate(657,304) rotate(-15) scale(1.5)"/>
      <use href="#bolt" fill="var(--sky)" transform="translate(147,464) rotate(-45) scale(1.3)"/>
      <use href="#bolt" fill="var(--sky)" transform="translate(622,484) rotate(25) scale(1.2)"/>
    </svg>

    <div class="crowd-haze"></div>
    <div class="crowd" role="img" aria-label="Black silhouette of a concert crowd with raised hands"></div>

    <h1 class="album-title">Copper Gulls</h1>
    <p class="album-subtitle">Broken Lantern Hour</p>
    <div class="volume-badge">VOL 2</div>
  </main>
</body>
</html>
```